Social Media Marketing website

Need website designed for social media marketing company BrightLoop.com
Do no currently have logo.
Pages:
Main
Services
Order
Contact
Please use dummy text for now. I will provide content to winner later to add.
Main page should clearly show the steps with some sort of graphic: Establish, Engage, Analyze.
Services provided (steps):
1) Establish social media presence
2) Social media management and advertising
3) Analyze and engage
Site should be simple, clean and attractive. Design examples:
http://plinkster.com/
http://www.quillbase.com/
http://www.harrowvalemq.com/
Be creative! It should not look like a template.
Updates
Updated examples.
Contact me for questions.
dave@brightloop.com
3) Analyze and engage
Advertising

```html
<!DOCTYPE html>
<html lang="en">
<head>
<meta charset="utf-8">
<title>BrightLoop.com – Social Media Marketing</title>
<link rel="stylesheet" href="https://fonts.googleapis.com/css2?family=Open+Sans:wght@300;400;600;700&family=Arimo:wght@400;700&family=Montserrat:wght@600&display=swap">
<style>
:root{
  --ink:#3a3a3a;
  --muted:#6b6b6b;
  --light:#9a9a9a;
  --teal:#1f8ea6;
  --teal-dark:#16768c;
  --teal-light:#46bccf;
  --orange:#ff8a00;
  --orange-light:#ffb21e;
  --header-top:#2b2b2b;
  --header-bottom:#141414;
  --rule:#e2e2e2;
  --band:#ebebeb;
  --footer:#ededed;
  --bar:#6a6a6a;
  --white:#ffffff;
}
*{box-sizing:border-box;margin:0;padding:0}
html,body{width:1050px;height:1200px;overflow:hidden;background:var(--white)}
body{position:relative;font-family:"Arimo",Arial,sans-serif;color:var(--ink)}
.abs{position:absolute}
h2,h3{font-family:"Arimo",Arial,sans-serif;font-weight:700;color:var(--ink)}
ul{list-style:none}

/* header */
.site-header{position:absolute;left:0;top:0;width:1050px;height:69px;background:linear-gradient(var(--header-top),var(--header-bottom));border-bottom:1px solid #000}
.brand{position:absolute;left:102px;top:20px;font-family:"Open Sans",sans-serif;font-weight:600;font-size:24px;color:var(--white);letter-spacing:-.5px;display:flex;align-items:center;gap:8px}
.brand-dot{width:12px;height:12px;border-radius:50%;background:var(--teal-light)}
.main-nav{position:absolute;left:507px;top:0;display:flex;height:69px}
.main-nav a{display:flex;align-items:center;justify-content:center;gap:8px;height:69px;font-family:"Montserrat",sans-serif;font-weight:600;font-size:11px;color:var(--white);text-decoration:none;border-left:1px solid #333;border-right:1px solid #0c0c0c;letter-spacing:.3px}
.main-nav a.active{background:#111;position:relative}
.main-nav a.active::after{content:"";position:absolute;bottom:-7px;left:50%;margin-left:-6px;border:6px solid transparent;border-top-color:#111;border-bottom:0}

/* hero */
.hero{position:absolute;left:0;top:70px;width:1050px;height:324px;overflow:hidden;background:radial-gradient(ellipse 520px 330px at 560px 320px,#4bbccd,#2496ad 60%,#1c8197)}
.hero-ring{position:absolute;border-radius:50%;background:rgba(255,255,255,.08)}
.hero-title{position:absolute;left:102px;top:66px;font-family:"Open Sans",sans-serif;font-weight:300;font-size:38px;line-height:37px;color:var(--white)}
.hero-title b{font-weight:700}
.hero-text{position:absolute;left:102px;top:155px;width:380px;font-size:10.5px;line-height:16px;color:var(--white)}
.btn-orange{position:absolute;display:flex;align-items:center;justify-content:center;background:linear-gradient(var(--orange-light),var(--orange));color:var(--white);font-family:"Arimo",sans-serif;border:1px solid #f07a00;border-radius:2px;box-shadow:0 1px 2px rgba(0,0,0,.2)}
.hero-btn{left:102px;top:218px;width:171px;height:39px;font-size:20px}
.hero-art{position:absolute;left:686px;top:74px;width:180px;height:180px;border-radius:50%;background:radial-gradient(circle at 40% 35%,#7fd36a,#3a9bd8 55%,#1d5f9e)}

/* steps */
.steps{position:absolute;left:0;top:394px;width:1050px;height:118px;background:var(--band);border-bottom:1px solid #dcdcdc}
.steps-notch{position:absolute;left:228px;top:394px;border:10px solid transparent;border-top-color:#2091a9;border-bottom:0}
.step{position:absolute;top:0;height:118px;background:linear-gradient(#fbfbfb,#efefef);border-left:1px solid #ddd}
.step-icon{position:absolute;left:16px;top:18px;width:44px;height:44px}
.step h3{position:absolute;left:76px;top:22px;font-size:16px;line-height:18px;font-weight:400;color:#333}
.step p{position:absolute;left:76px;top:63px;font-size:10.5px;line-height:16px;color:var(--muted)}

/* content */
.section-title{position:absolute;font-size:16px}
.copy{position:absolute;font-size:10.5px;line-height:17.5px;color:var(--muted)}
.btn-teal{position:absolute;display:flex;align-items:center;justify-content:center;background:linear-gradient(#2a9bb2,var(--teal-dark));color:var(--white);font-size:10.5px;border-radius:2px}
.rule{position:absolute;height:1px;background:var(--rule)}
.bullets li{position:relative;padding-left:15px;font-size:10.5px;line-height:21px;color:var(--muted)}
.bullets li::before{content:"";position:absolute;left:1px;top:8px;border:3px solid transparent;border-left:4px solid var(--teal);border-right:0}
.column-shade{position:absolute;left:672px;top:540px;width:6px;height:410px;background:linear-gradient(90deg,rgba(0,0,0,.04),transparent)}
.signup{left:102px;top:900px;width:345px;height:39px;font-size:20px}
.tour{position:absolute;left:461px;top:910px;font-size:12px;font-weight:700;color:var(--ink)}
.tour a{margin-left:8px;font-size:16px;color:var(--teal-dark);text-decoration:none}
.video{position:absolute;left:706px;top:589px;width:211px;height:144px;background:linear-gradient(#2a2118,#0d0b09);box-shadow:0 1px 4px rgba(0,0,0,.4)}
.testimonial-name{position:absolute;left:707px;top:885px;font-size:10.5px;font-weight:700;color:var(--teal-dark)}
.testimonial-name span{font-weight:400;color:var(--light);font-size:9.5px}

/* footer */
.site-footer{position:absolute;left:0;top:1006px;width:1050px;height:163px;background:linear-gradient(#e4e4e4,var(--footer) 30%);border-top:1px solid #d4d4d4}
.footer-col{position:absolute;top:24px}
.footer-col h3{font-size:16px;margin-bottom:6px}
.footer-sep{position:absolute;top:10px;width:1px;height:140px;background:#dadada}
.follow{display:flex;gap:9px;margin-top:9px}
.follow span{width:28px;height:28px;border-radius:3px;background:linear-gradient(var(--teal-light),var(--teal-dark))}
.copyright{position:absolute;left:0;top:1169px;width:1050px;height:31px;background:var(--bar);color:var(--white);font-size:10.5px;display:flex;align-items:center;justify-content:center}
</style>
</head>
<body>

<header class="site-header">
  <div class="brand"><span class="brand-dot"></span>BrightLoop.com</div>
  <nav class="main-nav">
    <a class="active" href="#" style="width:114px">
      <svg width="16" height="14" viewBox="0 0 16 14" aria-hidden="true"><path d="M8 0 0 7h2v7h4V9h4v5h4V7h2z" fill="#3fb6d6"/></svg>MAIN</a>
    <a href="#" style="width:114px">SERVICES</a>
    <a href="#" style="width:96px">ORDER</a>
    <a href="#" style="width:114px">CONTACT</a>
  </nav>
</header>

<section class="hero">
  <div class="hero-ring" style="left:356px;top:180px;width:250px;height:250px"></div>
  <div class="hero-ring" style="left:476px;top:130px;width:300px;height:300px"></div>
  <h1 class="hero-title"><b>Establish</b> social media<br>marketing <b>Presence</b></h1>
  <p class="hero-text">Lorem ipsum dolor sit amet, consectetuer adipiscing elit, sed diam nonummy nibh euismod tincidunt ut laoreet dolore magna aliquam erat volutpat.</p>
  <a class="btn-orange hero-btn">Get Order</a>
  <div class="hero-art" role="img" aria-label="Globe illustration surrounded by social network badges"></div>
</section>

<section class="steps">
  <div class="step" style="left:102px;width:274px">
    <div class="step-icon" role="img" aria-label="Small globe illustration" style="border-radius:50%;background:radial-gradient(circle at 40% 35%,#8fd66b,#2f8fd0)"></div>
    <h3>Establish Social Media<br>Presence</h3>
    <p>Lorem ipsum dolor sit amet,<br>consectetuer adipiscing elit, sed diam</p>
  </div>
  <div class="step" style="left:376px;width:299px">
    <div class="step-icon" role="img" aria-label="Profile document illustration" style="top:22px;height:40px;border-radius:3px;background:linear-gradient(#f4f7fa,#cfd9e2)"></div>
    <h3 style="left:80px">Social media management<br>and advertising</h3>
    <p style="left:80px">Lorem ipsum dolor sit amet,<br>consectetuer adipiscing elit, sed diam</p>
  </div>
  <div class="step" style="left:675px;width:270px">
    <svg class="step-icon" viewBox="0 0 44 44" aria-hidden="true">
      <circle cx="22" cy="22" r="21" fill="#7cc63a"/>
      <path d="M22 22 22 1A21 21 0 0 1 43 20Z" fill="#e83f8e"/>
      <path d="M22 22 43 20A21 21 0 0 1 36 38Z" fill="#f5c21b"/>
      <path d="M22 22 1 22A21 21 0 0 1 22 1Z" fill="#2d8fd5"/>
    </svg>
    <h3>Analyze &amp;<br>Engage</h3>
    <p>Lorem ipsum dolor sit amet,<br>consectetuer adipiscing elit, sed diam</p>
  </div>
</section>
<div class="steps-notch"></div>

<main>
  <h2 class="section-title" style="left:102px;top:548px">Why BrightLoop.com ?</h2>
  <p class="copy" style="left:102px;top:576px;width:530px">Lorem ipsum dolor sit amet, consectetuer adipiscing elit, sed diam nonummy nibh euismod tincidunt ut laoreet dolore magna aliquam erat volutpat. Ut wisi enim ad minim veniam, quis nostrud exerci tation ullamcorper suscipit lobortis nisl ut aliquip ex ea commodo consequat.</p>
  <a class="btn-teal" style="left:102px;top:639px;width:72px;height:19px">Learnmore</a>
  <div class="rule" style="left:102px;top:687px;width:528px"></div>

  <h2 class="section-title" style="left:102px;top:714px">Features</h2>
  <ul class="bullets abs" style="left:102px;top:740px">
    <li>Lorem ipsum dolor sit amet</li>
    <li>Consectetuer adipiscing elit, sed</li>
    <li>Diam nonummy nibh euismod tincidunt</li>
    <li>Ut laoreet dolore magna aliquam erat</li>
    <li>Volutpat ut wisi enim ad minim veniam,</li>
  </ul>
  <h2 class="section-title" style="left:382px;top:714px">Resource</h2>
  <ul class="bullets abs" style="left:382px;top:740px">
    <li>Lorem ipsum dolor sit amet</li>
    <li>Consectetuer adipiscing elit, sed</li>
    <li>Diam nonummy nibh euismod tincidunt</li>
    <li>Ut laoreet dolore magna aliquam erat</li>
    <li>Volutpat ut wisi enim ad minim veniam,</li>
  </ul>
  <div class="rule" style="left:102px;top:870px;width:528px"></div>

  <a class="btn-orange signup">Sign up now for a free 30-day trial</a>
  <p class="tour">or<a href="#">Take the Tour</a></p>

  <div class="column-shade"></div>

  <h2 class="section-title" style="left:706px;top:548px">Video Gallery</h2>
  <div class="video" role="img" aria-label="Video still of a presenter">
    <svg class="abs" style="left:76px;top:42px" width="60" height="60" viewBox="0 0 60 60" aria-hidden="true">
      <circle cx="30" cy="30" r="27" fill="rgba(0,0,0,.25)" stroke="#fff" stroke-width="4"/>
      <path d="M24 19v22l18-11z" fill="#fff"/>
    </svg>
  </div>
  <p class="copy" style="left:706px;top:751px;width:215px">Lorem ipsum dolor sit amet, consectetuer adipiscing elit, sed diam nonummy nibh .</p>
  <a class="btn-teal" style="left:706px;top:797px;width:72px;height:19px">Browse</a>
  <div class="rule" style="left:706px;top:837px;width:211px"></div>
  <h2 class="section-title" style="left:706px;top:855px">Testimonials</h2>
  <p class="testimonial-name">Harold <span>- May 2010</span></p>
  <p class="copy" style="left:707px;top:899px;width:215px">Lorem ipsum dolor sit amet, consectetuer adipiscing elit, sed diam nonummy nibh .</p>
</main>

<footer class="site-footer">
  <div class="footer-col" style="left:102px">
    <h3>News</h3>
    <ul class="bullets"><li>Lorem ipsum dolor sit amet</li><li>Consectetuer adipiscing elit,</li><li>Diam nonummy nibh euismod</li><li>Ut laoreet dolore magna</li></ul>
  </div>
  <div class="footer-sep" style="left:290px"></div>
  <div class="footer-col" style="left:328px">
    <h3>Partners</h3>
    <ul class="bullets"><li>Lorem ipsum dolor sit amet</li><li>Consectetuer adipiscing elit,</li><li>Diam nonummy nibh euismod</li><li>Ut laoreet dolore magna</li></ul>
  </div>
  <div class="footer-sep" style="left:517px"></div>
  <div class="footer-col" style="left:556px">
    <h3>Supports</h3>
    <ul class="bullets"><li>Support &amp; Services</li><li>Knowledge Baso</li><li>Log a case</li><li>Support Policy</li></ul>
  </div>
  <div class="footer-sep" style="left:701px"></div>
  <div class="footer-col" style="left:740px">
    <h3>Contact</h3>
    <p class="copy" style="position:static;line-height:20px">info@brightloop.com</p>
    <h3 style="margin-top:14px;margin-bottom:0">Follow Us</h3>
    <div class="follow"><span></span><span></span><span></span><span></span><span></span></div>
  </div>
</footer>
<div class="copyright">Copyright © 2011 BrightLoop.com All right reserved</div>

</body>
</html>
```